Forget what you know about corporate well

I need a one-page flies used for print, to embedding in a website, all social media platforms and email.

Target Market(s)

Business

Industry/Entity Type

Health And Wellness

Font styles to use
Serif
Script
Other font styles liked:
• I would like the designers opinion on the font

Colors

Designer to choose colors to be used in the design.

Requirements
Must have
• This is the wording:
• Did you know that 75% of healthcare costs are incurred by preventable diseases? Cardiovascular disease, cancer, and diabetes are the three major causes of rising health care plans and are all preventable.
• Owen and his team have spent decades learning how to increase productivity, reduce absenteeism, and increase employee engagement, all leading to lowering healthcare costs. Together, they have developed a system created to target the masses all while addressing individual needs. Their corporate training challenges helps to engrain positive habits through a carefully curated accountability and reward system.
• How it works:
• Step 1 – evaluate the needs of your business;
• Step 2 – set up individualized workshops based on highest needs;
• Step 3 – create a customized corporate training challenge.
• Why Owen?
• Owen excels at motivational speaking. He is an author, a nutritionist and a professional athlete with a master’s degree in clinical nutrition. He is a teacher of corporate wellness at Marbrook College and a health coach. Owen has been featured in national magazines, podcasts, and popular fitness websites. Owen’s own health issues put him on a quest to heal himself and others. With twenty-five years of experience and a passion for wellness, he can provide your company with an unforgettable experience.
Nice to have
• I will not give my opinion, I believe that is an insult to the designer. All of the verbiage is above and I attached a plethora of pictures.
Should not have
• No opinion

```html
<!DOCTYPE html>
<html lang="en">
<head>
<meta charset="utf-8">
<title>Brightpath Health – Corporate Wellness Flyer</title>
<link rel="stylesheet" href="https://fonts.googleapis.com/css2?family=Raleway:wght@400;500;700;800&display=swap">
<style>
  :root {
    --blue: #1f9be8;
    --lime: #cde63a;
    --green: #76c59a;
    --ink: #1b1b1b;
    --white: #ffffff;
    --brand-grey: #6a6a6a;
    --photo-dark: #5f5f5f;
    --photo-light: #8d8d8d;
    --gym-dark: #b9bcb4;
    --gym-light: #d8dad3;
  }
  * { margin: 0; padding: 0; box-sizing: border-box; }
  html, body { width: 895px; height: 1200px; overflow: hidden; background: var(--white); }
  .flyer {
    position: relative;
    width: 895px;
    height: 1200px;
    overflow: hidden;
    font-family: "Raleway", sans-serif;
    color: var(--ink);
  }
  .flyer-shapes { position: absolute; inset: 0; width: 895px; height: 1200px; }
  .headline {
    position: absolute;
    right: 209px;
    top: 60px;
    text-align: right;
    font-weight: 800;
    font-size: 25px;
    line-height: 23px;
    color: var(--white);
    text-shadow: 0 1px 3px rgba(0,0,0,.55);
    text-transform: uppercase;
  }
  .headline .accent { color: var(--lime); }
  .facts {
    position: absolute;
    left: 511px;
    top: 282px;
    width: 360px;
    color: var(--white);
  }
  .facts h2 {
    font-weight: 700;
    font-size: 27px;
    text-align: center;
    margin-bottom: 12px;
  }
  .facts p { font-size: 11.2px; line-height: 13.2px; letter-spacing: .1px; }
  .brand {
    position: absolute;
    left: 34px;
    top: 548px;
    display: flex;
    align-items: center;
    gap: 10px;
  }
  .brand-dot {
    width: 16px;
    height: 16px;
    border-radius: 50%;
    background: var(--lime);
  }
  .brand-name {
    font-weight: 700;
    font-size: 21px;
    color: var(--brand-grey);
  }
  .brand-owner {
    position: absolute;
    left: 60px;
    top: 586px;
    font-weight: 500;
    font-size: 17px;
    color: var(--brand-grey);
    letter-spacing: 1px;
  }
  .steps {
    position: absolute;
    left: 262px;
    top: 666px;
  }
  .steps h2 { font-weight: 700; font-size: 27px; margin-bottom: 14px; }
  .steps li {
    list-style: none;
    font-size: 16px;
    line-height: 17px;
    margin-bottom: 14px;
    font-weight: 500;
  }
  .steps strong { font-weight: 800; }
  .about {
    position: absolute;
    left: 39px;
    top: 860px;
    width: 378px;
    color: var(--white);
  }
  .about h2 { font-weight: 700; font-size: 27px; margin-bottom: 16px; }
  .about p { font-size: 16px; line-height: 22.6px; font-weight: 500; }
</style>
</head>
<body>
<main class="flyer">
  <svg class="flyer-shapes" viewBox="0 0 941 1328" preserveAspectRatio="none">
    <defs>
      <linearGradient id="portrait-tone" x1="0" y1="0" x2="1" y2="1">
        <stop offset="0" stop-color="#8d8d8d"/>
        <stop offset="1" stop-color="#5f5f5f"/>
      </linearGradient>
      <linearGradient id="session-tone" x1="0" y1="0" x2="1" y2="1">
        <stop offset="0" stop-color="#d8dad3"/>
        <stop offset="1" stop-color="#b9bcb4"/>
      </linearGradient>
    </defs>
    <rect class="paper" width="941" height="1328" fill="var(--white)"/>
    <polygon class="portrait-photo" role="img" aria-label="Photo of the coach smiling in a black t-shirt in front of a brick wall" points="0,0 941,0 941,40 0,565" fill="url(#portrait-tone)"/>
    <polygon class="session-photo" role="img" aria-label="Photo of a group wellness session in a fitness studio" points="90,815 498,580 941,830 941,1328 0,1328 0,800" fill="url(#session-tone)"/>
    <polygon class="facts-panel" points="380,430 941,97 941,760" fill="var(--blue)"/>
    <polyline class="facts-rule" points="941,83 343,430 941,775" fill="none" stroke="var(--lime)" stroke-width="7"/>
    <polyline class="frame-rule" points="0,290 510,582 90,815" fill="none" stroke="var(--blue)" stroke-width="6"/>
    <polygon class="about-panel" points="0,775 700,1160 560,1328 0,1328" fill="var(--blue)"/>
    <polygon class="corner-green" points="560,1328 700,1160 941,1100 941,1328" fill="var(--green)"/>
    <polygon class="corner-lime" points="700,1160 941,1015 941,1100" fill="var(--lime)" opacity=".55"/>
    <line class="corner-rule" x1="430" y1="1328" x2="941" y2="985" stroke="var(--lime)" stroke-width="8"/>
  </svg>

  <h1 class="headline">The Underground<br>Secret to <span class="accent">Permanent</span><br><span class="accent">Result</span></h1>

  <section class="facts">
    <h2>DID YOU KNOW?</h2>
    <p>75% of healthcare costs are incurred by preventable diseases? Cardiovascular disease, cancer, and diabetes are the three major causes of rising health care plans and are all preventable.<br>Owen and his team have spent decades learning how to increase productivity, reduce absenteeism, and increase employee engagement, all leading to lowering healthcare costs. Together, they have developed a system created to target the masses all while addressing individual needs. Their corporate training challenges helps to engrain positive habits through a carefully curated accountability and reward system.</p>
  </section>

  <div class="brand">
    <span class="brand-dot"></span>
    <p class="brand-name">Brightpath Health</p>
  </div>
  <p class="brand-owner">Owen Marlow</p>

  <section class="steps">
    <h2>HOW IT WORKS?</h2>
    <ul>
      <li><strong>Step 1</strong> – evaluate the needs of your business;</li>
      <li><strong>Step 2</strong> – set up individualized workshops based on highest needs;</li>
      <li><strong>Step 3</strong> – create a customized corporate training challenge.</li>
    </ul>
  </section>

  <section class="about">
    <h2>WHY OWEN?</h2>
    <p>Owen excels at motivational speaking. He is an author, a nutritionist and a professional athlete with a master’s degree in clinical nutrition. He is a teacher of corporate wellness at Marbrook College and a health coach. Owen has been featured in national magazines, podcasts, and popular fitness websites. Owen’s own health issues put him on a quest to heal himself and others. With twenty-five years of experience and a passion for wellness, he can provide your company with an unforgettable experience.</p>
  </section>
</main>
</body>
</html>
```